Consulting firm need a professional powerpoint design

A startup Climate change firm needs a powerpoint template design. The design should reflect aspects of climate change adaptation, resilience and environmental sustainability.

The powerpoint design must convey aspects of nature and climate action for a resilient society.

The last slide of the powerpoint must have a allocation for a slogan such as 'Linking science and decision-making'.

Use the colors in the logo and business card for the powerpoint design.

Target Market(s)

Government and industry

Font styles to use
Sans Serif
Other font styles liked:
• nexa font family

Colors
85cae6
abd037
fece3e

Requirements
Must have
• - Colors used in logo and business card
- Convey science and nature
- Professional
Nice to have
• Many pages
Should not have
• Not complicated

```html
<!DOCTYPE html>
<html lang="en">
<head>
<meta charset="utf-8">
<title>Infographics and Photos – Slide Template</title>
<link rel="stylesheet" href="https://fonts.googleapis.com/css2?family=Jost:wght@400&family=Roboto:wght@400;700&family=Montserrat:wght@800&display=swap">
<style>
  :root {
    --page-bg: #ffffff;
    --band: #e4f3f9;
    --ink: #1a1a1a;
    --navy: #2b3154;
    --leaf: #abd037;
    --fern-mid: #1f6b2e;
    --fern-light: #3c8c45;
    --fern-dark: #07200e;
    --sky-deep: #1f7fd8;
    --sky: #3f9ae6;
    --cloud: #d9ecfa;
    --grass-light: #b9b45a;
    --grass: #9c9a45;
    --grass-dark: #7d7d34;
    --emblem: #3fae4a;
    --white: #ffffff;
  }
  * { margin: 0; padding: 0; box-sizing: border-box; }
  html, body { width: 1200px; height: 240px; overflow: hidden; background: var(--page-bg); }
  .canvas { position: relative; width: 1200px; height: 240px; overflow: hidden; }
  .backdrop-band { position: absolute; inset: 0; }
  .section-heading {
    position: absolute; left: 20px; top: 16px;
    font-family: "Jost", sans-serif; font-weight: 400; font-size: 29px; line-height: 1;
    letter-spacing: 20.4px; color: var(--ink); white-space: nowrap;
  }
  .slide {
    position: absolute; top: 55px; width: 269px; height: 151px;
    background: var(--white);
    box-shadow: 0 5px 8px rgba(0, 0, 0, 0.12);
    overflow: hidden;
  }
  .slide--cover { left: 15px; }
  .slide--topic { left: 318px; outline: 1px solid #e6eef2; }
  .slide--closing { left: 621px; outline: 1px solid #e6eef2; }

  .cover-panel {
    position: absolute; left: 0; top: 0; width: 92px; height: 151px; background: var(--leaf);
  }
  .cover-title {
    position: absolute; left: 12px; top: 24px; width: 80px;
    font-family: "Roboto", sans-serif; font-weight: 700; font-size: 12.4px; line-height: 16.2px;
    color: var(--white);
  }
  .cover-photo {
    position: absolute; left: 95px; top: 0; width: 174px; height: 151px;
    background:
      radial-gradient(ellipse 45% 40% at 50% 50%, var(--fern-dark) 0%, rgba(7,32,14,0) 100%),
      linear-gradient(135deg, var(--fern-light) 0%, var(--fern-mid) 45%, #14461f 70%, var(--fern-light) 100%);
  }

  .topic-title {
    position: absolute; left: 12px; top: 10px;
    font-family: "Roboto", sans-serif; font-weight: 700; font-size: 8.8px; line-height: 11px;
    color: var(--navy); white-space: nowrap;
  }
  .topic-body {
    position: absolute; left: 13px; top: 36px;
    font-family: "Roboto", sans-serif; font-weight: 400; font-size: 4.6px; line-height: 5.95px;
    color: var(--ink); white-space: nowrap;
  }
  .topic-photo {
    position: absolute; left: 136px; top: 0; width: 133px; height: 151px;
    background:
      radial-gradient(ellipse 35% 18% at 40% 30%, rgba(255,255,255,0.75) 0%, rgba(255,255,255,0) 100%),
      radial-gradient(ellipse 40% 16% at 62% 52%, rgba(255,255,255,0.7) 0%, rgba(255,255,255,0) 100%),
      linear-gradient(172deg, var(--sky-deep) 0%, var(--sky) 40%, var(--cloud) 66%, var(--grass-light) 72%, var(--grass) 86%, var(--grass-dark) 100%);
  }

  .closing-slogan {
    position: absolute; left: 14px; top: 107px;
    font-family: "Montserrat", sans-serif; font-weight: 800; font-size: 15.2px; line-height: 17.8px;
    color: var(--navy); white-space: nowrap;
  }
  .closing-brand {
    position: absolute; left: 183px; top: 53px; width: 86px; height: 98px;
    display: flex; flex-direction: column; align-items: center; justify-content: center; gap: 8px;
  }
  .closing-brand__dot { width: 44px; height: 44px; border-radius: 50%; background: var(--emblem); }
  .closing-brand__name {
    font-family: "Montserrat", sans-serif; font-weight: 800; font-size: 9px; color: var(--navy);
    white-space: nowrap;
  }
</style>
</head>
<body>
<main class="canvas">
  <svg class="backdrop-band" width="1200" height="240" viewBox="0 0 1200 240" aria-hidden="true">
    <polygon points="70,240 347,240 1008,0 731,0" fill="var(--band)"/>
  </svg>

  <h1 class="section-heading">INFOGRAPHICS AND PHOTOS</h1>

  <section class="slide slide--cover">
    <div class="cover-panel"></div>
    <h2 class="cover-title">Please add title for slide here</h2>
    <div class="cover-photo" role="img" aria-label="Photo of dark green fern fronds"></div>
  </section>

  <section class="slide slide--topic">
    <h2 class="topic-title">Please add topic title here</h2>
    <p class="topic-body">Sed ut perspiciatis unde omnis iste natus error sit<br>voluptatem accusantium doloremque laudantium,<br>totam rem aperiam, eaque ipsa quae ab illo inventore<br>veritatis et quasi architecto beatae vitae dicta sunt<br>explicabo. Nemo enim ipsam voluptatem quia voluptas<br>sit aspernatur aut odit aut fugit, sed quia consequuntur<br>magni dolores eos qui ratione voluptatem sequi<br>nesciunt. Neque porro quisquam est.</p>
    <div class="topic-photo" role="img" aria-label="Photo of wind turbines on a grassy hill under a blue cloudy sky"></div>
  </section>

  <section class="slide slide--closing">
    <p class="closing-slogan">Linking science<br>&amp; decision-making</p>
    <div class="closing-brand">
      <span class="closing-brand__dot"></span>
      <span class="closing-brand__name">Verdant Shift</span>
    </div>
  </section>
</main>
</body>
</html>
```